Pitch book for the 2025 K7R Global Stunt Cup event in Muncie, Indiana, USA

Title: Fueling the Future of Aeromodeling: Sponsor the 2025 K7R Global Stunt Cup
1. Event Overview
What: The 2025 IVO K7R Global Stunt Cup for Aerobatic Model Aircraft.
When: August 9–16, 2025.
Where: Guild of Miniature Aircraft Pilots (GMP) Headquarters, Muncie, Indiana.
Hosted by: Guild of Miniature Aircraft Pilots (GMP) in partnership with the Continental League of Remote Piloted Stunts (CLRPS).
Participants: Top pilots from across the globe, including juniors and female competitors.
2. Why Sponsor?
Shaping the Future Workforce: Inspire youth to explore careers in aerospace, aviation, and unmanned systems (drones, RPVs), bridging hobbies and high-tech industries like Veltrax, Corvane Dynamics, and more.
Brand Visibility: Engage with a global audience of enthusiasts, professionals, and media at a premier international event.
Community Impact: Support an event that promotes innovation, STEM education, and cultural exchange.
3. Key Features of the Event
Cutting-Edge Venue: Over 1,100 acres of flying space tailored for precision aerobatics.
Diverse Competitions: Featuring junior and female classifications alongside world-class competitors.
Global Audience: Media coverage, live streams, and on-site spectators.
4. Sponsorship Opportunities
Title Sponsor ($50,000):
Naming rights: "Your Brand Presents the 2025 K7R Global Stunt Cup."
Logo placement on all event materials, website, and livestreams.
Prime exhibit space at the venue.
Gold Sponsor ($25,000):
Prominent branding on materials and media.
Speaking opportunity at the opening or closing ceremony.
Silver Sponsor ($10,000):
Recognition in event communications.
Inclusion in the sponsor wall at the venue.
Event Sponsor ($5,000):
Branding on specific activities (e.g., banquet, practice days).
Custom Sponsorships: Tailored to fit corporate goals, including STEM outreach and branded giveaways.
5. Audience Demographics
Competitors: Over 100 elite pilots from 40+ countries.
Spectators & Supporters: Thousands of attendees, ranging from hobbyists to industry professionals.
Media Reach: Coverage by international aeromodelling and aerospace outlets.
6. STEM and Industry Connections
Showcase pathways from aeromodelling to careers in aviation, engineering, and defense.
Collaborate with sponsors on outreach programs for local schools and universities.
7. Marketing Benefits
Digital: Inclusion in newsletters, website, and social media campaigns.
On-Site Branding: Banners, booths, and branded giveaways.
Networking: Access to high-value attendees and industry leaders.
8. Budget Breakdown
Goal: Raise $180,000 to support the championship.
Funding Allocation:
$70,000: Event logistics (venue, staff, equipment).
$50,000: Participant support (travel subsidies, junior competitor outreach).
$30,000: Marketing and media coverage.
$20,000: Amenities and hospitality.
9. Call to Action
Be Part of the Legacy: Join us in creating a memorable event that not only crowns world champions but also inspires future innovators.
Contact Information:
Name: [Your Name]
Email: [Your Email]
Phone: [Your Phone]
Website: [Event Website Link]

```html
<!DOCTYPE html>
<html lang="en">
<head>
<meta charset="utf-8">
<title>Sponsor the 2025 K7R Global Stunt Cup</title>
<link rel="stylesheet" href="https://fonts.googleapis.com/css2?family=Roboto+Condensed:wght@300;400;700&family=Kaushan+Script&display=swap">
<style>
  :root{
    --paper:#ffffff;
    --wine:#7a1c3e;
    --wine-deep:#4e1430;
    --berry:#9a2a52;
    --plum:#5c2342;
    --plum-deep:#3e1830;
    --ink:#ffffff;
    --ink-soft:rgba(255,255,255,.82);
  }
  *{margin:0;padding:0;box-sizing:border-box}
  html,body{width:1200px;height:2194px;overflow:hidden;background:var(--paper)}
  body{position:relative;font-family:"Roboto Condensed",Arial,sans-serif;color:var(--ink)}
  .page{position:absolute;left:244px;width:712px;height:1007px;overflow:hidden;box-shadow:0 6px 14px rgba(0,0,0,.28)}
  .page--cover{top:62px}
  .page--offer{top:1122px;height:1009px}
  .photo{position:absolute;inset:0}
  .photo--cover{background:radial-gradient(ellipse at 35% 55%,#8c3152 0%,var(--wine) 45%,var(--wine-deep) 100%)}
  .photo--planes{position:absolute;left:0;top:0;width:100%;height:280px;background:linear-gradient(180deg,#6e1a3a 0%,var(--berry) 55%,#b0405f 100%)}
  .photo--team{position:absolute;left:0;top:230px;width:100%;bottom:0;background:linear-gradient(180deg,var(--plum) 0%,#6a2648 55%,var(--plum-deep) 100%)}
  .wave{position:absolute;left:0;top:220px;width:100%;height:70px}
  .abs{position:absolute}
  .cover-title{left:38px;top:40px;width:420px;font-size:41px;font-weight:700;line-height:52px}
  .event-block{right:38px;top:260px;text-align:right}
  .event-name{font-size:23px;font-weight:700;line-height:31px}
  .event-date{margin-top:22px;font-size:40px;font-weight:700;line-height:46px}
  .event-place{margin-top:14px;font-size:23px;font-weight:300;line-height:31px}
  .hosted{left:38px;top:581px;width:460px;font-size:16px;line-height:22px}
  .hosted em{font-family:"Kaushan Script",cursive;font-style:normal}
  .participants{left:38px;top:664px;width:400px;font-size:15px;font-weight:700;line-height:20px}
  .section-head{font-size:23px;font-weight:700;line-height:30px}
  .why{left:38px;top:733px;width:640px}
  .features{left:38px;top:866px;width:640px}
  .points{margin-top:14px;list-style:none;font-size:12px;line-height:17px;font-weight:300;color:var(--ink-soft)}
  .points b{font-weight:700;color:var(--ink)}
  .offer-head{left:38px;top:36px;font-size:25px;font-weight:700}
  .tier-col{top:88px;width:340px}
  .tier-col--left{left:38px}
  .tier-col--right{left:412px;width:270px}
  .tier{margin-bottom:22px}
  .tier h3{font-size:15px;font-weight:700;line-height:19px}
  .tier p{font-size:10.5px;font-weight:300;line-height:14px;color:var(--ink-soft)}
  .col-rule{left:381px;top:92px;width:1px;height:118px;background:rgba(255,255,255,.55)}
  .info{left:38px;width:620px}
  .info h2{font-size:25px;font-weight:700;line-height:28px}
  .info p{font-size:10.5px;font-weight:300;line-height:14px;color:var(--ink-soft)}
  .contact{left:38px;top:890px}
  .contact h2{font-size:25px;font-weight:700}
  .contact-row{position:relative;margin-top:4px;height:26px;width:640px;font-size:19px;font-weight:300}
  .contact-row span{position:absolute;top:0}
</style>
</head>
<body>

<section class="page page--cover">
  <div class="photo photo--cover" role="img" aria-label="Close-up of an aerobatic model aircraft propeller and nose, tinted wine red"></div>

  <h1 class="abs cover-title">Fueling the Future of Aeromodeling: Sponsor the 2025 K7R Global Stunt Cup</h1>

  <div class="abs event-block">
    <p class="event-name">The 2025 IVO K7R Global Stunt Cup<br>for Aerobatic<br>Model Aircraft.</p>
    <p class="event-date">August 9–16, 2025</p>
    <p class="event-place">Location:<br>Guild of Miniature Aircraft Pilots<br>(GMP) Headquarters, Muncie, Indiana.</p>
  </div>

  <p class="abs hosted"><em>Hosted by:</em> Guild of Miniature Aircraft Pilots (GMP) in partnership with the Continental League of Remote Piloted Stunts (CLRPS).</p>

  <p class="abs participants">Participants: Top pilots from across the globe, including juniors and female competitors.</p>

  <div class="abs why">
    <h2 class="section-head">Why Sponsor?</h2>
    <ul class="points">
      <li><b>Shaping the Future Workforce:</b> Inspire youth to explore careers in aerospace, aviation, and unmanned systems (drones, RPVs), bridging hobbies and high-tech industries like Veltrax, Corvane Dynamics, and more.</li>
      <li><b>Brand Visibility:</b> Engage with a global audience of enthusiasts, professionals, and media at a premier international event.</li>
      <li>Community Impact: Support an event that promotes innovation, STEM education, and cultural exchange.</li>
    </ul>
  </div>

  <div class="abs features">
    <h2 class="section-head">Key Features of the Event</h2>
    <ul class="points">
      <li><b>Cutting-Edge Venue:</b> Over 1,100 acres of flying space tailored for precision aerobatics.</li>
      <li><b>Diverse Competitions:</b> Featuring junior and female classifications alongside world-class competitors.</li>
      <li><b>Global Audience:</b> Media coverage, live streams, and on-site spectators.</li>
    </ul>
  </div>
</section>

<section class="page page--offer">
  <div class="photo photo--planes" role="img" aria-label="Rows of aerobatic model aircraft parked on grass, tinted red"></div>
  <div class="photo photo--team" role="img" aria-label="Smiling pilots and supporters holding a model aircraft, tinted plum"></div>
  <svg class="wave" viewBox="0 0 712 70" preserveAspectRatio="none" aria-hidden="true">
    <path d="M0 40 C180 5 420 5 712 30 L712 70 L0 70 Z" fill="#5c2342"/>
    <path d="M0 40 C180 5 420 5 712 30" fill="none" stroke="rgba(255,255,255,.35)" stroke-width="1.5"/>
  </svg>

  <h2 class="abs offer-head">Sponsorship Opportunities</h2>

  <div class="abs tier-col tier-col--left">
    <div class="tier">
      <h3>Title Sponsor ($50,000):</h3>
      <p>Naming rights: "Your Brand Presents the 2025 K7R Global Stunt Cup."<br>Logo placement on all event materials, website, and livestreams.<br>Prime exhibit space at the venue.</p>
    </div>
    <div class="tier">
      <h3>Gold Sponsor ($25,000):</h3>
      <p>Prominent branding on materials and media.<br>Speaking opportunity at the opening or closing ceremony.</p>
    </div>
  </div>
  <div class="abs col-rule"></div>
  <div class="abs tier-col tier-col--right">
    <div class="tier">
      <h3>Silver Sponsor ($10,000):</h3>
      <p>Recognition in event communications.<br>Inclusion in the sponsor wall at the venue.</p>
    </div>
    <div class="tier">
      <h3>Event Sponsor ($5,000):</h3>
      <p>Branding on specific activities (e.g., banquet, practice days).<br>Custom Sponsorships: Tailored to fit corporate goals, including STEM outreach and branded giveaways.</p>
    </div>
  </div>

  <div class="abs info" style="top:340px">
    <h2>Audience Demographics</h2>
    <p>Competitors: Over 100 elite pilots from 40+ countries.<br>Spectators &amp; Supporters: Thousands of attendees, ranging from hobbyists to industry professionals.<br>Media Reach: Coverage by international aeromodelling and aerospace outlets.</p>
  </div>
  <div class="abs info" style="top:431px">
    <h2>STEM and Industry Connections</h2>
    <p>Showcase pathways from aeromodelling to careers in aviation, engineering, and defense.<br>Collaborate with sponsors on outreach programs for local schools and universities.</p>
  </div>
  <div class="abs info" style="top:509px">
    <h2>Marketing Benefits</h2>
    <p>Digital: Inclusion in newsletters, website, and social media campaigns.<br>On-Site Branding: Banners, booths, and branded giveaways.<br>Networking: Access to high-value attendees and industry leaders.</p>
  </div>
  <div class="abs info" style="top:602px">
    <h2>Budget Breakdown</h2>
    <p>Goal: Raise $180,000 to support the championship.<br>Funding Allocation:<br>$70,000: Event logistics (venue, staff, equipment).<br>$50,000: Participant support (travel subsidies, junior competitor outreach).<br>$30,000: Marketing and media coverage.<br>$20,000: Amenities and hospitality.</p>
  </div>
  <div class="abs info" style="top:779px">
    <h2>Call to Action</h2>
    <p>Be Part of the Legacy: Join us in creating a memorable event that not only crowns world champions but also inspires future innovators.</p>
  </div>

  <div class="abs contact">
    <h2>Contact Information:</h2>
    <div class="contact-row">
      <span style="left:0">5550142025</span>
      <span style="left:176px">sponsor@stuntcup-example.org</span>
      <span style="left:420px">www.stuntcup-example.org</span>
    </div>
  </div>
</section>

</body>
</html>
```